Business Card Design for Venture Kite

Venture Kite is a pro bono student consultancy service offered by Corvala KTRB to social start ups and enterprises. We provide consulting services with expertise in areas such as Marketing, IT, Business Strategy and Innovation.
I have attached\ the Venture Kite Logo here for your perusal.
Industry/Entity Type
Business
Contact Information for Business Card
Name: Ha Min Park Name: Thomas Leung
Role: Project Leader Role: Vice Project Leader
M:0477203941 M: 0479352806
E: ha-min.park@corvalaktrb.org E: thomas.leung@corvalaktrb.org
W: www.corvalaktrb.org W: www.corvalaktrb.org

```html
<!DOCTYPE html>
<html lang="en">
<head>
<meta charset="utf-8">
<title>Venture Kite – Business Card</title>
<link rel="stylesheet" href="https://fonts.googleapis.com/css2?family=Ubuntu:ital,wght@0,400;0,500;0,700;1,400;1,700&display=swap">
<style>
  :root {
    --orange: #e08a1e;
    --paper: #f5f4f1;
    --ink: #1c1c1c;
    --backdrop: #d8d8d6;
  }
  html, body {
    margin: 0;
    width: 1200px;
    height: 1000px;
    overflow: hidden;
    background: var(--backdrop);
  }
  .sheet {
    position: relative;
    width: 1200px;
    height: 1000px;
  }
  .card {
    position: absolute;
    left: 250px;
    width: 700px;
    height: 400px;
    box-shadow: 0 6px 18px rgba(0,0,0,0.18);
    background: var(--paper);
  }
  .card--front { top: 60px; }
  .card--back { top: 540px; }
  .card svg { display: block; }
  .fill-orange { fill: var(--orange); }
  .fill-paper { fill: var(--paper); }
  .wordmark {
    font-family: "Ubuntu", sans-serif;
    font-weight: 700;
    fill: var(--ink);
  }
  .person-name {
    font-family: "Ubuntu", sans-serif;
    font-weight: 700;
    font-style: italic;
    font-size: 24px;
  }
  .person-role {
    font-family: "Ubuntu", sans-serif;
    font-style: italic;
    font-size: 17px;
  }
  .contact {
    font-family: "Ubuntu", sans-serif;
    font-size: 16px;
    fill: var(--paper);
  }
  .is-orange { fill: var(--orange); }
  .is-paper { fill: var(--paper); }
</style>
</head>
<body>
<main class="sheet">

  <!-- Front of card -->
  <section class="card card--front" aria-label="Card front">
    <svg width="700" height="400" viewBox="0 0 700 400">
      <rect class="fill-paper" width="700" height="400"/>
      <polygon class="fill-orange" points="0,35 545,35 590,0 700,0 700,338 300,338 258,400 0,400"/>
      <rect class="fill-paper" x="240" y="112" width="225" height="178"/>
      <text class="wordmark" x="352" y="210" font-size="30" text-anchor="middle">Venture Kite</text>
    </svg>
  </section>

  <!-- Back of card -->
  <section class="card card--back" aria-label="Card back">
    <svg width="700" height="400" viewBox="0 0 700 400">
      <rect class="fill-paper" width="700" height="400"/>
      <rect class="fill-orange" width="700" height="12"/>

      <polygon class="fill-orange" points="0,92 450,92 418,138 700,138 700,238 0,238"/>
      <polygon class="fill-orange" points="330,262 700,262 700,372 145,372"/>
      <polygon class="fill-orange" points="0,338 175,338 155,372 0,372"/>

      <text class="person-name is-orange" x="70" y="58">Ha Min Park</text>
      <text class="person-role is-orange" x="112" y="80">Project Leader</text>

      <text class="contact" x="52" y="124">M : 047- 720- 3941</text>
      <text class="contact" x="52" y="150">E : ha-min.park@corvalaktrb.org</text>
      <text class="contact" x="52" y="176">W : www.corvalaktrb.org</text>

      <text class="wordmark" x="598" y="122" font-size="19" text-anchor="middle">Venture Kite</text>

      <text class="person-name is-paper" x="645" y="182" text-anchor="end">Thomas Leung</text>
      <text class="person-role is-paper" x="645" y="205" text-anchor="end" font-style="normal">Vice Project Leader</text>

      <text class="contact" x="645" y="298" text-anchor="end">M : 047- 935- 2806</text>
      <text class="contact" x="645" y="324" text-anchor="end">W : www.corvalaktrb.org</text>
      <text class="contact" x="645" y="350" text-anchor="end">E : thomas.leung@corvalaktrb.org</text>
    </svg>
  </section>

</main>
</body>
</html>
```